Book Cover for a Story of War, Survival, and Victory

I need a book cover that defines the experience of a girl of 12 years of age going through war with their family, becoming a refugee and surviving trauma and abuse. This is a story of survival and victory. It is a true story based on the first Liberian war that lasted from 1989 to 1991! The story is confronting, honest and motivational as the one who went through these things survived and overcame. She is a motivator and encourager. This book will be self-published online. Please do not hesitate to ask any questions.

Font styles to use
Serif

Requirements
Must have
• Must have below title & subtitle
• Title: Her Quiet Harbor
• Subtitle: A Passage Through Storm To Calm
• Author: J.K. Halden
Nice to have
• Striking, bold and strong. Eye catching in a good way. Would like to see some variations.
• Story is set in Rural Liberia not the city.
Should not have
• Clashing colours

```html
<!DOCTYPE html>
<html lang="en">
<head>
<meta charset="utf-8">
<title>Her Quiet Harbor — Book Cover</title>
<link rel="stylesheet" href="https://fonts.googleapis.com/css2?family=Anton&family=Jost:wght@400;700&display=swap">
<style>
  :root {
    --stage: #9a9a9a;
    --stage-light: #e6e6e6;
    --storm-dark: #0e161d;
    --storm-mid: #3a464d;
    --haze: #eef2f2;
    --sea-red: #c63a22;
    --sea-deep: #9e2218;
    --shore-pink: #d9a6a2;
    --salt: #f4f1ec;
    --title-red: #b3141c;
    --white: #ffffff;
    --ink: #1b1b1b;
  }
  * { box-sizing: border-box; margin: 0; padding: 0; }
  html, body { width: 1200px; height: 1000px; overflow: hidden; }
  body {
    background: linear-gradient(180deg, var(--stage-light) 0%, var(--stage) 100%);
    position: relative;
  }
  .cover {
    position: absolute;
    left: 280px;
    top: 20px;
    width: 640px;
    height: 960px;
    overflow: hidden;
    box-shadow: 0 10px 30px rgba(0,0,0,0.3);
  }
  .cover-art {
    position: absolute;
    inset: 0;
    background:
      linear-gradient(180deg,
        var(--storm-dark) 0%,
        var(--storm-mid) 18%,
        #9aa6a8 30%,
        var(--white) 42%,
        var(--haze) 56%,
        var(--sea-red) 62%,
        var(--sea-deep) 74%,
        #b0573c 79%,
        var(--salt) 83%,
        var(--shore-pink) 92%,
        #c98d87 100%);
  }
  .title {
    position: absolute;
    left: 18px;
    top: 20px;
    height: 700px;
    writing-mode: vertical-rl;
    transform: rotate(180deg);
    font-family: "Anton", "Impact", sans-serif;
    font-size: 98px;
    line-height: 1;
    letter-spacing: 1px;
    color: var(--title-red);
    -webkit-text-stroke: 3px var(--white);
    paint-order: stroke fill;
    text-transform: uppercase;
    white-space: nowrap;
  }
  .subtitle {
    position: absolute;
    left: 150px;
    top: 548px;
    font-family: "Jost", "Futura", sans-serif;
    font-weight: 400;
    font-size: 28px;
    color: var(--ink);
    white-space: nowrap;
  }
  .author {
    position: absolute;
    right: 40px;
    top: 640px;
    font-family: "Jost", "Futura", sans-serif;
    font-weight: 700;
    font-size: 26px;
    line-height: 1.1;
    color: var(--white);
    text-align: center;
  }
</style>
</head>
<body>
  <main class="cover">
    <div class="cover-art" role="img" aria-label="Photograph of dark storm clouds breaking over a bright sky above a red sea meeting a pale salt shoreline"></div>
    <h1 class="title">Her Quiet Harbor</h1>
    <p class="subtitle">A Passage Through Storm To Calm</p>
    <p class="author">Author<br>J.K. Halden</p>
  </main>
</body>
</html>
```